Create a flyer design (10cm X 21cm) for an aquarium in France

We are a public aquarium in France and we want announcing the events of christmas holidays
We invite you to create our flyer recto (just the front side).

The size of this flyer is : 10cm X 21cm
Have a look on flyer.doc to know texts...
We want also get the flyer in original version (.psd, .ai) please.

We remain at your disposal for any question.
Thanks.

Industry/Entity Type

Events

Requirements
Must have
• The text must be written in french, you will find attached all the text that you have to fill in the flyer.
• You also have to use our logo in the top or in the bottom of the flyer (2 versions of the logo four color or black and white version. According your design you can use one of them)
• You must specify our website and our adress.
• Have a look on flyer.doc to know texts...

```html
<!DOCTYPE html>
<html lang="fr">
<head>
<meta charset="utf-8">
<title>Aquarium de Kerlune – Vacances de Noël</title>
<link href="https://fonts.googleapis.com/css2?family=Nunito:wght@700;800;900&display=swap" rel="stylesheet">
<style>
:root{
  --navy:#1f3a5c;
  --sea-top:#6f9a94;
  --sea-mid:#3f7a70;
  --sea-deep:#1d4a42;
  --sand:#6b6a55;
  --suit-red:#9a2a2a;
  --suit-dark:#5c1c1e;
  --reef:#2a2a24;
  --band:rgba(255,255,255,0.62);
  --band-edge:rgba(255,255,255,0.92);
  --link-blue:#2f6fa8;
  --ring:rgba(230,234,236,0.78);
  --contact:#4c6680;
  --brand:#2f7fb0;
}
*{margin:0;padding:0;box-sizing:border-box}
html,body{width:1200px;height:2514px;overflow:hidden;background:#fff}
.flyer{
  position:relative;width:1200px;height:2514px;overflow:hidden;
  font-family:'Nunito',sans-serif;
}
.scene{
  position:absolute;inset:0;
  background:
    radial-gradient(ellipse 190px 120px at 860px 1430px, rgba(25,25,28,0.75), rgba(25,25,28,0) 100%),
    radial-gradient(ellipse 250px 620px at 560px 1500px, rgba(154,42,42,0.95), rgba(154,42,42,0.75) 55%, rgba(154,42,42,0) 100%),
    radial-gradient(ellipse 300px 420px at 420px 1350px, rgba(120,30,32,0.85), rgba(120,30,32,0) 100%),
    radial-gradient(ellipse 170px 420px at 640px 2050px, rgba(92,28,30,0.9), rgba(92,28,30,0) 100%),
    radial-gradient(ellipse 240px 200px at 320px 500px, rgba(170,40,40,0.55), rgba(170,40,40,0) 100%),
    radial-gradient(ellipse 420px 380px at 200px 1760px, rgba(42,42,36,0.95), rgba(42,42,36,0.6) 60%, rgba(42,42,36,0) 100%),
    radial-gradient(ellipse 900px 380px at 600px 2514px, rgba(120,112,84,0.9), rgba(120,112,84,0) 100%),
    linear-gradient(180deg,var(--sea-top) 0%,var(--sea-mid) 30%,var(--sea-deep) 60%,#2f4a3c 82%,var(--sand) 100%);
}
.brand-cap{
  position:absolute;left:100px;top:-270px;width:910px;height:530px;border-radius:50%;
  background:radial-gradient(ellipse at 50% 70%,rgba(255,255,255,0.96),rgba(232,240,243,0.88));
}
.brand-name{
  position:absolute;top:92px;left:100px;width:910px;text-align:center;
  color:var(--brand);font-weight:900;font-size:56px;line-height:1;
}
.brand-sub{
  position:absolute;top:162px;left:100px;width:910px;text-align:center;
  color:var(--brand);font-weight:900;font-size:20px;letter-spacing:4px;text-transform:uppercase;
}
.events{position:absolute;left:0;top:0;width:1200px}
.event{
  position:absolute;left:14px;width:1172px;height:54px;
  background:linear-gradient(180deg,var(--band-edge) 0,var(--band-edge) 4px,var(--band) 12px,rgba(255,255,255,0.5));
  display:flex;align-items:center;padding-left:16px;
  color:var(--navy);font-weight:800;font-size:30px;white-space:nowrap;
}
.event svg{width:32px;height:32px;margin-right:20px;flex:none}
.info-link{
  position:absolute;left:325px;top:1372px;width:862px;height:56px;
  background:rgba(255,255,255,0.62);
  display:flex;align-items:center;justify-content:center;
  color:var(--link-blue);font-weight:800;font-size:25px;
}
.photo-ring{position:absolute;border-radius:50%;background:var(--ring)}
.photo{position:absolute;border-radius:50%}
.ring-large{left:646px;top:1512px;width:530px;height:530px}
.photo-large{left:676px;top:1542px;width:470px;height:470px;
  background:radial-gradient(circle at 55% 45%,#6a5a72,#1c3d55 70%,#0f2b3c)}
.ring-small{left:62px;top:1988px;width:462px;height:462px}
.photo-small{left:92px;top:2018px;width:402px;height:402px;
  background:radial-gradient(circle at 50% 55%,#c9c35a,#6b7f70 55%,#4a5f62)}
.contact{
  position:absolute;left:790px;top:2228px;width:410px;height:240px;
  background:rgba(255,255,255,0.62);
  padding:34px 40px 0 0;text-align:right;
  color:var(--contact);font-weight:800;font-size:28px;line-height:1.4;
}
</style>
</head>
<body>
<div class="flyer">
  <div class="scene" role="img" aria-label="Photo sous-marine d'un plongeur déguisé en Père Noël nourrissant des poissons au-dessus d'un récif et du sable"></div>

  <div class="brand-cap"></div>
  <div class="brand-name">Aquarium de Kerlune</div>
  <div class="brand-sub">Baie des Lunes</div>

  <div class="events">
    <div class="event" style="top:350px"><svg viewBox="0 0 32 32"><circle cx="16" cy="16" r="13" fill="none" stroke="#1f3a5c" stroke-width="4"/><circle cx="16" cy="16" r="5" fill="#1f3a5c"/></svg>Nourrissages commentés de nos espèces aquatiques chaque après-midi</div>
    <div class="event" style="top:468px"><svg viewBox="0 0 32 32"><circle cx="16" cy="16" r="13" fill="none" stroke="#1f3a5c" stroke-width="4"/><circle cx="16" cy="16" r="5" fill="#1f3a5c"/></svg>Vos vacances de Noël à l'aquarium</div>
    <div class="event" style="top:580px"><svg viewBox="0 0 32 32"><circle cx="16" cy="16" r="13" fill="none" stroke="#1f3a5c" stroke-width="4"/><circle cx="16" cy="16" r="5" fill="#1f3a5c"/></svg>Animations &lt;&lt;bassin tactile&gt;&gt; commentees plusieurs fois par jour</div>
    <div class="event" style="top:678px"><svg viewBox="0 0 32 32"><circle cx="16" cy="16" r="13" fill="none" stroke="#1f3a5c" stroke-width="4"/><circle cx="16" cy="16" r="5" fill="#1f3a5c"/></svg>Atelier scientifique sur les requins lundi 28 decembre</div>
    <div class="event" style="top:784px"><svg viewBox="0 0 32 32"><circle cx="16" cy="16" r="13" fill="none" stroke="#1f3a5c" stroke-width="4"/><circle cx="16" cy="16" r="5" fill="#1f3a5c"/></svg>Plongée du Père-Noël les 22 et 23 décembre</div>
    <div class="event" style="top:898px"><svg viewBox="0 0 32 32"><circle cx="16" cy="16" r="13" fill="none" stroke="#1f3a5c" stroke-width="4"/><circle cx="16" cy="16" r="5" fill="#1f3a5c"/></svg>Nocturne, une visite drôle et décalée, mardi 29 décembre</div>
    <div class="event" style="top:1006px"><svg viewBox="0 0 32 32"><circle cx="16" cy="16" r="13" fill="none" stroke="#1f3a5c" stroke-width="4"/><circle cx="16" cy="16" r="5" fill="#1f3a5c"/></svg>Fish manucure, les 29, 30 et 31 décembre</div>
    <div class="event" style="top:1112px"><svg viewBox="0 0 32 32"><circle cx="16" cy="16" r="13" fill="none" stroke="#1f3a5c" stroke-width="4"/><circle cx="16" cy="16" r="5" fill="#1f3a5c"/></svg>Dégustation vitaminée, les 2 et 3 janvier</div>
  </div>

  <div class="info-link">Retrouvez toutes les informations via aquariumdekerlune.fr</div>

  <div class="photo-ring ring-large"></div>
  <div class="photo photo-large" role="img" aria-label="Photo d'un poisson tacheté de blanc sur fond sombre"></div>

  <div class="photo-ring ring-small"></div>
  <div class="photo photo-small" role="img" aria-label="Photo d'un poisson-coffre jaune à cornes"></div>

  <div class="contact">
    Aquarium de Kerlune<br>
    14, rue des Mouettes<br>
    56000 KERLUNE<br>
    02 91 23 45 67
  </div>
</div>
</body>
</html>
```